indépendant en tant que Massothérapeute et Préparateur Mental, j'ai besoin de ...

Massothérapeute et préparateur mental indépendant, je recherche une carte de visite sobre et dynamique, sans images liées au massage ou à la préparation mentale mais intégrant mon logo. Les couleurs que j'aime bien sont : Blanc, gris, anthracite, noir et jaune

Contact Information for Business Card

carte de préférence Horizontale
neutre qui puisse toucher le deux domaines Massothérapie et préparation mentale

Requirements
Must have
• mon projet doit intégrer au recto:
LOGO
Loïc Vermande
078 315 26 49
info@loicvermande-exemple.ch
et éventuellement www.loicvermande-exemple.ch

et au verso les deux adresses:

Chemin des Ormelets 27B
1400 Yverdon-les-Bains

Rue des Tanneries 9
1700 Fribourg

Should not have
• mon projet ne doit pas contenir d'image en liens avec le massage ni la préparation mentale.

```html
<!DOCTYPE html>
<html lang="fr">
<head>
<meta charset="utf-8">
<title>Loïc Vermande – Cartes de visite</title>
<link rel="stylesheet" href="https://fonts.googleapis.com/css2?family=Work+Sans:wght@400;500;600&display=swap">
<style>
  :root {
    --stage: #2b2b2b;
    --card-light: #e9e8e6;
    --photo-a: #f2f1ef;
    --photo-b: #c9c3bf;
    --photo-c: #a8a09c;
    --anthracite-1: #1b1b1b;
    --anthracite-2: #3a3a3a;
    --yellow: #f5b915;
    --ink: #1e1e1e;
    --white: #ffffff;
    --muted: #d8d8d8;
  }
  * { box-sizing: border-box; margin: 0; padding: 0; }
  html, body { width: 1200px; height: 930px; overflow: hidden; }
  body {
    background: var(--stage);
    font-family: "Work Sans", Arial, sans-serif;
    position: relative;
  }
  .card {
    position: absolute;
    width: 540px;
    height: 310px;
    border-radius: 22px;
    overflow: hidden;
    box-shadow: 0 18px 40px rgba(0,0,0,.45);
  }
  .card--front { left: 60px; top: 110px; background: var(--card-light); }
  .card--back {
    left: 600px; top: 500px;
    background: linear-gradient(100deg, var(--anthracite-1) 0%, var(--anthracite-2) 55%, var(--anthracite-1) 100%);
  }
  .photo-fill {
    position: absolute; inset: 0;
    background: radial-gradient(ellipse at 45% 55%, var(--photo-c) 0%, var(--photo-b) 35%, var(--photo-a) 80%);
    opacity: .75;
  }
  .brand {
    position: absolute;
    display: flex; flex-direction: column;
    color: var(--ink);
    white-space: nowrap;
  }
  .brand__name {
    font-weight: 600; letter-spacing: .02em;
    display: flex; align-items: center; gap: 10px;
  }
  .brand__dot { width: 14px; height: 14px; border-radius: 50%; background: var(--ink); }
  .brand__tag { font-weight: 500; text-transform: uppercase; letter-spacing: .06em; }
  .card--front .brand { left: 120px; top: 128px; }
  .card--front .brand__name { font-size: 30px; }
  .card--front .brand__tag { font-size: 10px; margin-top: 4px; margin-left: 24px; }

  .back-visual { position: absolute; left: 300px; top: -60px; width: 400px; height: 400px; }
  .card--back .brand { left: 362px; top: 126px; }
  .card--back .brand__name { font-size: 18px; gap: 8px; }
  .card--back .brand__dot { width: 11px; height: 11px; }
  .card--back .brand__tag { font-size: 6.5px; letter-spacing: .04em; margin-top: 3px; margin-left: 19px; }

  .contact { position: absolute; left: 36px; top: 44px; color: var(--white); }
  .contact__name { color: var(--yellow); font-size: 26px; line-height: 31px; font-weight: 600; letter-spacing: .03em; text-transform: uppercase; }
  .contact__role { font-size: 15px; line-height: 18px; color: var(--muted); margin-top: 2px; }
  .contact__list { list-style: none; margin-top: 14px; font-size: 14.5px; }
  .contact__list li { display: flex; align-items: center; gap: 9px; line-height: 21px; }
  .contact__list svg { width: 12px; height: 12px; flex: none; }
  .address { margin-top: 12px; font-size: 14.5px; line-height: 20px; font-style: normal; }
  .address + .address { margin-top: 8px; }
</style>
</head>
<body>

  <section class="card card--front" aria-label="Recto">
    <div class="photo-fill" role="img" aria-label="Photo douce en tons gris clair et beige"></div>
    <div class="brand">
      <span class="brand__name"><span class="brand__dot"></span>Loïc Vermande</span>
      <span class="brand__tag">Massothérapeute / Préparateur Mental</span>
    </div>
  </section>

  <section class="card card--back" aria-label="Verso">
    <svg class="back-visual" viewBox="0 0 400 400" aria-hidden="true">
      <defs>
        <radialGradient id="circle-photo" cx="45%" cy="55%" r="60%">
          <stop offset="0" stop-color="#a8a09c"/>
          <stop offset=".4" stop-color="#cbc5c1"/>
          <stop offset="1" stop-color="#efeeec"/>
        </radialGradient>
      </defs>
      <circle cx="210" cy="200" r="190" fill="#eeeeee"/>
      <path d="M40 120 A190 190 0 0 0 150 380" fill="none" stroke="var(--yellow)" stroke-width="7" stroke-linecap="round"/>
      <circle cx="212" cy="200" r="184" fill="url(#circle-photo)" role="img" aria-label="Photo douce en tons gris clair et beige"/>
    </svg>
    <div class="brand">
      <span class="brand__name"><span class="brand__dot"></span>Loïc Vermande</span>
      <span class="brand__tag">Massothérapeute / Préparateur Mental</span>
    </div>

    <div class="contact">
      <h1 class="contact__name">Loïc Vermande</h1>
      <p class="contact__role">Director</p>
      <ul class="contact__list">
        <li>
          <svg viewBox="0 0 12 12"><path d="M3 1l2 2.5-1.2 1.2a7 7 0 0 0 3.5 3.5L8.5 7 11 9l-1 2C5 11 1 7 1 2z" fill="var(--yellow)"/></svg>
          078 315 26 49
        </li>
        <li>
          <svg viewBox="0 0 12 12"><rect x="1" y="2.5" width="10" height="7" rx="1" fill="none" stroke="var(--yellow)" stroke-width="1.3"/><path d="M1.5 3l4.5 3.5L10.5 3" fill="none" stroke="var(--yellow)" stroke-width="1.3"/></svg>
          info@loicvermande-exemple.ch
        </li>
        <li>
          <svg viewBox="0 0 12 12"><circle cx="6" cy="6" r="5" fill="none" stroke="var(--yellow)" stroke-width="1.2"/><path d="M1 6h10M6 1c-2.5 3-2.5 7 0 10M6 1c2.5 3 2.5 7 0 10" fill="none" stroke="var(--yellow)" stroke-width="1"/></svg>
          www.loicvermande-exemple.ch
        </li>
      </ul>
      <address class="address">Chemin des Ormelets 27B<br>1400 Yverdon-les-Bains</address>
      <address class="address">Rue des Tanneries 9<br>1700 Fribourg</address>
    </div>
  </section>

</body>
</html>
```